Business Card Design for a technology company

Our current business card is outdated and stale.

We need a new look and one soon.

We're a telematics (GPS tracking) company based in Australia. Our audiences are transport and logistics company.

Target Market(s)

1. Transport and Logistics Companies
2. Food and Beverage Manufacturers
3. Concrete Businesses

Industry/Entity Type

Logistics

Contact Information for Business Card

Lumen Rove

Font styles to use
Sans Serif

Colors
3276b5
0255a3
85acd3
cfdeed
ffffff

Requirements
Must have
• Logo
• "Premium Suppliers of Real Time Temperature Tracking"
• Contact Name
• Business Title
• Address
• Telephone
• Mobile
• Email
• Website URL
Nice to have
• Visual representation of tracking or maps.
Should not have
• Image of a satellite as currently shown

```html
<!DOCTYPE html>
<html lang="en">
<head>
<meta charset="utf-8">
<title>Lumen Rove — Business Cards</title>
<link rel="stylesheet" href="https://fonts.googleapis.com/css2?family=Roboto:ital,wght@0,400;0,500;1,400&family=Roboto+Condensed:wght@700&display=swap">
<style>
  :root {
    --backdrop: #e4e4e4;
    --card-white: #f7f7f7;
    --brand-blue: #0255a3;
    --name-blue: #0a3f8f;
    --mid-blue: #3276b5;
    --light-blue: #85acd3;
    --pale-blue: #cfdeed;
    --white: #ffffff;
    --body-grey: #4a4a4a;
    --tag-grey: #3a3a3a;
    --rule-grey: #cfcfcf;
  }
  * { margin: 0; padding: 0; box-sizing: border-box; }
  html, body { width: 1200px; height: 799px; overflow: hidden; }
  body {
    position: relative;
    background: var(--backdrop);
    font-family: "Roboto", Arial, sans-serif;
  }
  .card {
    position: absolute;
    width: 542px;
    height: 308px;
    background: var(--card-white);
  }
  .card--front-a { left: 46px; top: 78px; }
  .card--front-b { left: 615px; top: 78px; }
  .card--back {
    left: 331px; top: 428px; height: 310px;
    background: radial-gradient(ellipse 60% 70% at 50% 40%, var(--mid-blue) 0%, #1a62ab 45%, var(--brand-blue) 100%);
    overflow: hidden;
  }

  .brand {
    position: absolute;
    text-align: right;
  }
  .brand__name {
    display: block;
    font-family: "Roboto", Arial, sans-serif;
    font-weight: 500;
    font-size: 42px;
    line-height: 1;
    letter-spacing: -0.5px;
    color: var(--brand-blue);
    white-space: nowrap;
  }
  .brand__tagline {
    display: block;
    margin-top: 6px;
    font-size: 13px;
    line-height: 16px;
    color: var(--tag-grey);
  }
  .brand__promise {
    display: block;
    font-size: 12.5px;
    line-height: 16px;
    font-style: italic;
    color: var(--tag-grey);
  }
  .card--front-a .brand { right: 280px; top: 125px; }
  .card--front-b .brand { right: 268px; top: 125px; }

  .divider {
    position: absolute;
    top: 52px;
    width: 1px;
    height: 200px;
    background: var(--rule-grey);
  }
  .card--front-a .divider { left: 287px; }
  .card--front-b .divider { left: 300px; }

  .contact { position: absolute; color: var(--body-grey); font-size: 13px; line-height: 16px; }
  .card--front-a .contact { left: 311px; top: 54px; }
  .card--front-b .contact { left: 324px; top: 63px; }

  .contact__name {
    font-family: "Roboto Condensed", "Arial Narrow", sans-serif;
    font-weight: 700;
    font-size: 20px;
    line-height: 22px;
    color: var(--name-blue);
    margin-bottom: 8px;
    letter-spacing: 0.2px;
  }
  .contact__company, .contact__address { margin-bottom: 5px; }
  .contact__list { list-style: none; margin-top: 7px; }
  .contact__item {
    display: flex;
    align-items: center;
    height: 17.5px;
  }
  .contact__icon {
    width: 11px; height: 11px;
    margin-right: 8px;
    fill: var(--name-blue);
    flex: none;
  }

  .back__brand {
    position: absolute;
    left: 0; right: 0; top: 140px;
    text-align: center;
    font-weight: 500;
    font-size: 52px;
    line-height: 1;
    letter-spacing: -0.5px;
    color: var(--white);
  }
  .back__map {
    position: absolute;
    left: 20px; top: 10px; width: 500px; height: 240px;
    background: radial-gradient(ellipse at 50% 45%, rgba(207,222,237,0.18), rgba(133,172,211,0.06) 70%, transparent 100%);
  }
  .back__claim {
    position: absolute;
    left: 0; right: 0; top: 262px;
    text-align: center;
    font-size: 13.5px;
    color: var(--white);
    letter-spacing: 0.1px;
  }
</style>
</head>
<body>

<svg width="0" height="0" style="position:absolute" aria-hidden="true">
  <symbol id="icon-phone" viewBox="0 0 12 12">
    <path d="M2.3 0.6 4 2.3c.3.3.3.8 0 1.1L3.2 4.2c.6 1.4 1.6 2.5 3 3.2l.8-.8c.3-.3.8-.3 1.1 0l1.7 1.7c.3.3.3.8 0 1.1l-1 1C8.2 11 7.5 11.2 6.9 11 3.9 10 1.7 7.8.8 4.8.6 4.2.8 3.5 1.2 3.1l1.1-2.5z"/>
  </symbol>
  <symbol id="icon-mobile" viewBox="0 0 12 12">
    <path d="M3 0h6a1 1 0 0 1 1 1v10a1 1 0 0 1-1 1H3a1 1 0 0 1-1-1V1a1 1 0 0 1 1-1zm.4 1.4v7.8h5.2V1.4zM6 9.8a.7.7 0 1 0 0 1.4.7.7 0 0 0 0-1.4z"/>
  </symbol>
  <symbol id="icon-fax" viewBox="0 0 12 12">
    <path d="M3 0h6v3.5H3zM1 4.5h10a1 1 0 0 1 1 1V9H0V5.5a1 1 0 0 1 1-1zM0 10h12v2H0zM9.5 5.5a.6.6 0 1 0 0 1.2.6.6 0 0 0 0-1.2z"/>
  </symbol>
  <symbol id="icon-mail" viewBox="0 0 12 12">
    <path d="M0 2.5h12v.6L6 7 0 3.1zM0 4.3l6 3.9 6-3.9V10H0z"/>
  </symbol>
  <symbol id="icon-web" viewBox="0 0 12 12">
    <path d="M6 0a6 6 0 1 0 0 12A6 6 0 0 0 6 0zm-.6 1.3c-.5.4-1.2.6-1.3 1.3.4.4 1 .2 1.4.6-.3.6-1.2.5-1.5 1.1.3.8 1.5.5 1.9 1.2.3.7-.3 1.4 0 2.1.3.9.5 1.8.3 2.7A4.7 4.7 0 0 1 1.4 5c.6-.4 1.4-.2 1.7-.9C3.3 3.1 2.8 2.6 3.4 2a4.7 4.7 0 0 1 2-.7zm2.2.3A4.7 4.7 0 0 1 10.7 6c-.5.4-1.2.3-1.6-.2-.4-.6 0-1.5-.6-2-.4-.4-1.1-.2-1.3-.8-.2-.5.2-1 .4-1.4z"/>
  </symbol>
</svg>

<section class="card card--front-a" aria-label="Business card front, Marcus Delaney">
  <div class="brand">
    <span class="brand__name">Lumen Rove</span>
    <span class="brand__tagline">Your eye in the sky</span>
    <span class="brand__promise">Watch and Monitor on the Web 24/7</span>
  </div>
  <div class="divider"></div>
  <div class="contact">
    <p class="contact__name">MARCUS DELANEY</p>
    <p class="contact__company">Lumen Rove Rentals Pty Ltd<br>48 302 615 904</p>
    <p class="contact__address">7,41 Larkfield Road<br>Kelmont VIC 3188</p>
    <ul class="contact__list">
      <li class="contact__item"><svg class="contact__icon"><use href="#icon-phone"/></svg>+61 3 9400 2186</li>
      <li class="contact__item"><svg class="contact__icon"><use href="#icon-mobile"/></svg>+61 0412 555 304</li>
      <li class="contact__item"><svg class="contact__icon"><use href="#icon-fax"/></svg>+61 3 9400 2187</li>
      <li class="contact__item"><svg class="contact__icon"><use href="#icon-mail"/></svg>mdelaney@lumenrove.com.au</li>
      <li class="contact__item"><svg class="contact__icon"><use href="#icon-web"/></svg>www.lumenrove.com.au</li>
    </ul>
  </div>
</section>

<section class="card card--front-b" aria-label="Business card front, Priya Halvorsen">
  <div class="brand">
    <span class="brand__name">Lumen Rove</span>
    <span class="brand__tagline">Your eye in the sky</span>
    <span class="brand__promise">Watch and Monitor on the Web 24/7</span>
  </div>
  <div class="divider"></div>
  <div class="contact">
    <p class="contact__name">PRIYA HALVORSEN</p>
    <p class="contact__company">Lumen Rove Rentals Pty Ltd<br>48 302 615 904</p>
    <p class="contact__address">7,41 Larkfield Road<br>Kelmont VIC 3188</p>
    <ul class="contact__list">
      <li class="contact__item"><svg class="contact__icon"><use href="#icon-phone"/></svg>+61 3 9400 2186</li>
      <li class="contact__item"><svg class="contact__icon"><use href="#icon-mobile"/></svg>+61 0421 555 718</li>
      <li class="contact__item"><svg class="contact__icon"><use href="#icon-fax"/></svg>+61 3 9400 2187</li>
      <li class="contact__item"><svg class="contact__icon"><use href="#icon-web"/></svg>www.lumenrove.com.au</li>
    </ul>
  </div>
</section>

<section class="card card--back" aria-label="Business card back">
  <div class="back__map" role="img" aria-label="Faint world map spread across the card background"></div>
  <p class="back__brand">Lumen Rove</p>
  <p class="back__claim">Premium Suppliers of Real Time Temperature Tracking</p>
</section>

</body>
</html>
```